Website for a dog poop removal service.

The Fernwick Folks specializes in professional and hassle-free pet waste removal services, ensuring your yard stays clean, fresh, and safe for your family and pets. We take care of the dirty work, so you don’t have to, offering reliable, scheduled cleanups tailored to your needs. Let us help you reclaim your time and enjoy a spotless, stress-free outdoor space!
We will need the winning website to be transferred to our domain located at Valtorix. We would like to have the following web pages.
Home
About
Services
Contact Us
Client Portal
FAQ
Blog
Free Quote
The Free Quote webpage and client portal will need to be integrated with the following our account on the following website: tallowfen.com

```html
<!DOCTYPE html>
<html lang="en">
<head>
<meta charset="utf-8">
<title>The Fernwick Folks — Pet Waste Removal</title>
<link href="https://fonts.googleapis.com/css2?family=Lato:wght@400;700;900&display=swap" rel="stylesheet">
<style>
:root{
  --green:#5a9e2f;
  --green-dark:#3f7d1f;
  --brown:#b5835f;
  --ink:#1f1f1f;
  --muted:#444;
  --faq:#ececec;
  --beige:#efe4da;
  --footer:#1c1c1c;
  --white:#fff;
}
*{box-sizing:border-box;margin:0;padding:0}
html,body{width:1200px;height:4785px;overflow:hidden;background:var(--white)}
body{position:relative;font-family:'Lato',sans-serif;color:var(--ink)}
.abs{position:absolute}
.ph{position:absolute}
.btn{position:absolute;display:flex;align-items:center;justify-content:center;background:var(--brown);color:#fff;font-weight:700;font-size:15px;border-radius:3px}
.mascot{display:inline-block;width:38px;height:38px;border-radius:50%;background:#d9e8cc;vertical-align:middle;margin-right:8px}
.sec-title{position:absolute;left:0;width:1200px;text-align:center;font-size:42px;font-weight:700;color:var(--ink)}
.sec-title .hl{color:var(--green)}

/* header */
.logo{left:90px;top:22px;display:flex;align-items:center;gap:10px}
.logo-mark{width:64px;height:64px;border-radius:50%;background:#d9e8cc}
.logo-name{font-size:21px;font-weight:900;color:var(--ink);line-height:1.05;width:150px}
.nav{left:395px;top:40px;display:flex;gap:0;font-size:14px}
.nav a{color:var(--ink);text-decoration:none;padding:7px 10px;margin-right:6px}
.nav a.active{background:var(--green);color:#fff;border-radius:3px}

/* hero */
.hero{left:34px;top:114px;width:1132px;height:600px;border-radius:22px;overflow:hidden;background:linear-gradient(100deg,#4f7a32 0%,#6c9a45 45%,#a6b98a 75%,#7f9f5c 100%)}
.hero h1{position:absolute;left:73px;top:126px;font-size:52px;line-height:68px;font-weight:900;color:#fff;width:520px}
.hero p{position:absolute;left:76px;top:345px;font-size:22px;line-height:32px;color:#fff;width:420px}
.hero .b1{left:78px;top:438px;width:211px;height:43px}
.hero .b2{left:311px;top:438px;width:288px;height:43px;background:transparent;border:2px solid #fff}
.dots{position:absolute;left:532px;top:540px;display:flex;gap:8px}
.dots span{width:11px;height:11px;border-radius:50%;background:rgba(0,0,0,.35)}
.dots span:first-child{background:#fff}

/* benefits */
.benefit{position:absolute;top:878px;width:240px;text-align:center}
.benefit .icon{width:96px;height:96px;border-radius:50%;background:var(--beige);margin:0 auto 22px}
.benefit h3{font-size:20px;font-weight:700;line-height:25px}

/* about */
.about h2{left:640px;top:1140px;font-size:42px;font-weight:700}
.about p{position:absolute;left:640px;width:445px;font-size:14.5px;line-height:22px;color:var(--muted)}

/* services */
.svc{position:absolute;top:1752px;width:226px;text-align:center}
.svc .img{width:226px;height:235px;border-radius:2px}
.svc h3{font-size:21px;font-weight:700;margin-top:20px}
.svc p{font-size:14px;line-height:22px;color:var(--muted);margin-top:6px}

/* why */
.why{left:34px;top:2207px;width:1132px;height:575px;border-radius:18px;overflow:hidden;background:linear-gradient(90deg,#5a9e2f 0%,#62a435 55%,#6aa63e 100%)}
.why h2{position:absolute;left:101px;top:108px;font-size:38px;color:#fff;font-weight:700}
.why-list{position:absolute;left:0;top:0}
.why-item{position:absolute;left:97px;display:flex;align-items:center}
.why-item .num{width:52px;height:52px;border-radius:50%;background:#fff;color:var(--green);font-size:26px;font-weight:700;display:flex;align-items:center;justify-content:center;margin-right:32px}
.why-item h4{font-size:18px;color:#fff;font-weight:700}
.why-item p{font-size:13px;color:#eaf3e0}

/* faq */
.faq-item{position:absolute;left:244px;width:712px;height:60px;background:var(--faq);border:1px solid #dcdcdc;display:flex;align-items:center;justify-content:space-between;padding:0 28px;color:var(--green);font-size:19px;font-weight:500}
.faq-item span.t{font-size:20px}
.faq-answer{position:absolute;left:278px;top:3052px;width:640px;font-size:15px;line-height:22px;color:#333}

/* testimonials */
.tcard{position:absolute;top:3778px;width:317px;height:227px;border:1px solid #e6e6e6;border-radius:6px;padding:28px 24px;background:#fff;box-shadow:0 2px 8px rgba(0,0,0,.05)}
.tcard.featured{background:var(--green);color:#fff;border-color:var(--green)}
.stars{color:#e59b2a;font-size:16px;letter-spacing:1px}
.tcard.featured .stars{color:#fff}
.tcard p{font-size:14.5px;line-height:22px;margin-top:14px;color:#444}
.tcard.featured p{color:#fff}
.tcard h5{font-size:16px;font-weight:700;margin-top:16px}
.tcard small{font-size:12px;display:block;margin-top:6px}

/* footer */
.footer{left:0;top:4355px;width:1200px;height:430px;background:var(--footer);color:#fff}
.fcol{position:absolute;top:86px}
.fcol h4{font-size:20px;font-weight:700;margin-bottom:28px}
.fcol p,.fcol li{font-size:14px;line-height:25px;color:#eee;list-style:none}
.fcol li{margin-bottom:13px;line-height:20px}
.contact-row{display:flex;gap:16px;font-size:14px;line-height:22px;margin-bottom:28px}
.contact-row svg{flex:none;margin-top:2px}
.socials{display:flex;gap:14px;margin-top:30px}
.socials span{width:36px;height:36px;border-radius:6px;background:#3a3a3a}
.socials span:first-child{background:var(--green)}
.copy{position:absolute;left:0;top:4385px}
</style>
</head>
<body>

<!-- header -->
<div class="abs logo">
  <div class="logo-mark"></div>
  <div class="logo-name">THE FERNWICK FOLKS</div>
</div>
<nav class="abs nav">
  <a class="active">Home</a><a>About</a><a>Services</a><a>Contact Us</a><a>Client Portal</a><a>FAQ</a><a>Blog</a>
</nav>
<div class="btn" style="left:968px;top:36px;width:119px;height:42px">Free Quote</div>

<!-- hero -->
<section class="abs hero" role="img" aria-label="Photo of a smiling woman and girl hugging a golden retriever on a sunny lawn">
  <h1>Keeping Your Yard Clean, Fresh, and Hassle-Free!</h1>
  <p>Professional pet waste removal services tailored to your needs.</p>
  <div class="btn b1">Get a Free Quote Today!</div>
  <div class="btn b2">Schedule Your First Cleanup Now!</div>
  <div class="dots"><span></span><span></span><span></span><span></span></div>
</section>

<!-- benefits -->
<h2 class="sec-title" style="top:806px"><span class="mascot" role="img" aria-label="Small cartoon dog mascot"></span>Key <span class="hl">Benefits</span></h2>
<div class="ph" style="left:15px;top:920px;width:120px;height:180px;background:linear-gradient(180deg,#e9e4de,#cfc6bc);border-radius:40px" role="img" aria-label="Photo of a border collie sitting"></div>
<div class="benefit" style="left:80px"><div class="icon" role="img" aria-label="Scheduled cleanup icon"></div><h3>Reliable, Scheduled Cleanups</h3></div>
<div class="benefit" style="left:352px"><div class="icon" role="img" aria-label="Safe for pets shield icon"></div><h3>Safe for Pets and Family</h3></div>
<div class="benefit" style="left:604px"><div class="icon" role="img" aria-label="Hassle-free badge icon"></div><h3>Affordable and Hassle-free</h3></div>
<div class="benefit" style="left:872px"><div class="icon" role="img" aria-label="Eco-friendly disposal icon"></div><h3>Environmentally Responsible Disposal</h3></div>

<!-- about -->
<div class="ph" style="left:111px;top:1131px;width:437px;height:441px;border-radius:4px;background:linear-gradient(160deg,#7c9b5a,#5a7c3b 60%,#9fb27e)" role="img" aria-label="Photo of a small white dog on grass with its owner sitting behind"></div>
<section class="about">
  <h2 class="abs"><span class="mascot" role="img" aria-label="Small cartoon dog mascot"></span>About <span style="color:var(--green)">Us</span></h2>
  <p style="top:1223px">We’re passionate about making life easier for pet owners. Our professional team is dedicated to ensuring your yard stays clean, healthy, and stress-free. With flexible scheduling, affordable rates, and top-notch customer service, we make pet ownership even more enjoyable.</p>
  <p style="top:1361px">The Fernwick Folks specializes in professional and hassle-free pet waste removal services, ensuring your yard stays clean, fresh, and safe for your family and pets. We take care of the dirty work, so you don’t have to, offering reliable, scheduled cleanups tailored to your needs. Let us help you reclaim your time and enjoy a spotless, stress-free outdoor space!</p>
  <div class="btn" style="left:640px;top:1528px;width:142px;height:42px">Read More</div>
</section>
<div class="ph" style="left:955px;top:1490px;width:190px;height:255px;border-radius:50%;background:radial-gradient(#f2f2f2,#e2e2e2 60%,#fff 72%)" role="img" aria-label="Photo of a white terrier standing on its hind legs"></div>

<!-- services -->
<h2 class="sec-title" style="top:1664px"><span class="mascot" role="img" aria-label="Small cartoon dog mascot"></span>Our Services <span class="hl">Tailored to Your Needs</span></h2>
<div class="svc" style="left:111px"><div class="img" style="background:linear-gradient(160deg,#c94a6a,#e0a030 45%,#5d8c3a)" role="img" aria-label="Photo of a wheelbarrow and garden tools on a lawn"></div><h3>Weekly Cleanups</h3><p>Keep your yard spotless with our regular cleanup services. Ideal for maintaining a fresh and clean outdoor space.</p></div>
<div class="svc" style="left:362px"><div class="img" style="background:linear-gradient(160deg,#8fae6a,#6f8f4c 50%,#3b7fb4)" role="img" aria-label="Photo of a terrier holding a garden trowel"></div><h3>One-Time Cleanups</h3><p>Need help before a special event or after a busy week? We’ve got you covered with our one-time cleanup service.</p></div>
<div class="svc" style="left:612px"><div class="img" style="background:linear-gradient(160deg,#b9c98f,#d9cdb2 50%,#7e9b5a)" role="img" aria-label="Photo of two children sitting on grass with a small dog"></div><h3>Custom Schedules</h3><p>Choose a schedule that fits your lifestyle. We offer flexible options to ensure your yard stays pristine.</p></div>
<div class="svc" style="left:862px"><div class="img" style="background:linear-gradient(160deg,#4f6e33,#6b8a45 50%,#c23a3a)" role="img" aria-label="Photo of children playing with a dog in a park"></div><h3>Commercial Services</h3><p>Perfect for parks, apartment complexes, and other dog-friendly spaces. Let us handle the mess while you focus on your property.</p></div>

<!-- why choose us -->
<section class="abs why">
  <div class="ph" style="left:660px;top:0;width:472px;height:575px;background:radial-gradient(ellipse at 55% 55%,#e4b98a 0%,#d19d68 28%,rgba(106,166,62,0) 60%)" role="img" aria-label="Photo of a golden retriever puppy on a red leash"></div>
  <h2><span class="mascot" role="img" aria-label="Small cartoon dog mascot"></span>Why Choose Us?</h2>
  <svg class="abs" style="left:123px;top:232px" width="4" height="245"><line x1="2" y1="0" x2="2" y2="245" stroke="#fff" stroke-width="2"/></svg>
  <div class="why-item" style="top:194px"><div class="num">01</div><div><h4>Reliable Service:</h4><p>Always on time, always thorough.</p></div></div>
  <div class="why-item" style="top:275px"><div class="num">02</div><div><h4>Pet &amp; Eco-Friendly:</h4><p>Safe disposal methods and eco-conscious practices.</p></div></div>
  <div class="why-item" style="top:356px"><div class="num">03</div><div><h4>Satisfaction Guaranteed:</h4><p>We’re not happy unless you’re happy!</p></div></div>
  <div class="why-item" style="top:437px"><div class="num">04</div><div><h4>Locally Owned &amp; Operated:</h4><p>Supporting our community, one yard at a time.</p></div></div>
</section>

<!-- faq -->
<div class="ph" style="left:0;top:3380px;width:1200px;height:220px;background:linear-gradient(180deg,rgba(255,255,255,0) 0%,#a9c97a 40%,#5f9a32 100%)" role="img" aria-label="Photo of tall green grass"></div>
<div class="ph" style="left:25px;top:2815px;width:205px;height:235px;border-radius:50%;background:radial-gradient(#eef3e8,#d6e6c6 60%,rgba(255,255,255,0) 72%)" role="img" aria-label="Cartoon dog holding a pooper scooper"></div>
<div class="ph" style="left:980px;top:3175px;width:205px;height:240px;border-radius:50%;background:radial-gradient(#eef3e8,#d6e6c6 60%,rgba(255,255,255,0) 72%)" role="img" aria-label="Cartoon dog holding a pooper scooper"></div>
<h2 class="abs" style="left:286px;top:2876px;font-size:42px;font-weight:700"><span class="mascot" role="img" aria-label="Small cartoon dog mascot"></span>Frequently Asked&nbsp; <span style="color:var(--green)">Questions?</span></h2>
<div class="faq-item" style="top:2975px"><span>What does your dog poop removal service include</span><span class="t">–</span></div>
<p class="faq-answer">A1: Our service includes locating, scooping, and disposing of dog waste from your yard or designated area. We ensure your space is left clean and sanitary.</p>
<div class="faq-item" style="top:3125px"><span>Do you service all yard sizes?</span><span class="t">+</span></div>
<div class="faq-item" style="top:3205px"><span>How often can I schedule your services?</span><span class="t">+</span></div>
<div class="faq-item" style="top:3285px"><span>Are you environmentally friendly?</span><span class="t">+</span></div>
<div class="btn" style="left:530px;top:3373px;width:141px;height:42px">View All</div>

<!-- testimonials -->
<h2 class="sec-title" style="top:3690px"><span class="mascot" role="img" aria-label="Small cartoon dog mascot"></span>What Our <span class="hl">Customers Say</span></h2>
<div class="tcard" style="left:111px"><div class="stars">★★★★★</div><p>Excepteur sint occaecat cupidatat non proident, sunt in culpa qui officia deserunt mollit anim id est laborum.</p><h5>Hollister</h5><small>Jan 04 2024</small></div>
<div class="tcard featured" style="left:441px"><div class="stars">★★★★★</div><p>Excepteur sint occaecat cupidatat non proident, sunt in culpa qui officia deserunt mollit anim id est laborum.</p><h5>Wren</h5><small>Jan 04 2024</small></div>
<div class="tcard" style="left:771px"><div class="stars">★★★★★</div><p>Excepteur sint occaecat cupidatat non proident, sunt in culpa qui officia deserunt mollit anim id est laborum.</p><h5>Odessa</h5><small>Jan 04 2024</small></div>

<!-- cta -->
<div class="ph" style="left:10px;top:4050px;width:180px;height:305px;border-radius:45%;background:linear-gradient(180deg,#d8d8d8,#8a8a8a)" role="img" aria-label="Photo of a border collie sitting"></div>
<div class="ph" style="left:990px;top:4130px;width:160px;height:225px;border-radius:45%;background:linear-gradient(180deg,#e2b884,#c48a52)" role="img" aria-label="Photo of a golden retriever puppy sitting"></div>
<h2 class="sec-title" style="top:4082px"><span class="mascot" role="img" aria-label="Small cartoon dog mascot"></span>Let’s Keep Your <span class="hl">Yard Clean!</span></h2>
<p class="abs" style="left:300px;top:4160px;width:600px;text-align:center;font-size:19px;line-height:26px;color:#333">Ready to schedule your cleanup or have questions? We’d love to hear from you.</p>
<div class="btn" style="left:530px;top:4233px;width:141px;height:42px">Free Quote!</div>

<!-- footer -->
<footer class="abs footer">
  <div class="fcol" style="left:114px;width:290px">
    <h4>About Us</h4>
    <p>We’re passionate about making life easier for pet owners. Our professional team is dedicated to ensuring your yard stays clean, healthy, and stress-free.</p>
    <div class="socials" aria-label="Social links"><span></span><span></span><span></span><span></span></div>
  </div>
  <div class="fcol" style="left:455px;width:260px">
    <h4>Contact Us</h4>
    <div class="contact-row"><svg width="20" height="22" viewBox="0 0 20 22"><path d="M10 1a7 7 0 0 0-7 7c0 5 7 13 7 13s7-8 7-13a7 7 0 0 0-7-7z" fill="none" stroke="#fff" stroke-width="1.6"/><circle cx="10" cy="8" r="2.5" fill="none" stroke="#fff" stroke-width="1.6"/></svg><span>4820 W Larkspur Ct.<br>Meadowvale, ID 83790</span></div>
    <div class="contact-row"><svg width="20" height="20" viewBox="0 0 20 20"><path d="M4 2l3 0 2 5-2 1.5a10 10 0 0 0 4.5 4.5L13 11l5 2v3a2 2 0 0 1-2 2C9 18 2 11 2 4a2 2 0 0 1 2-2z" fill="none" stroke="#fff" stroke-width="1.6"/></svg><span>(555) 014-7722</span></div>
    <div class="contact-row"><svg width="20" height="16" viewBox="0 0 20 16"><rect x="1" y="1" width="18" height="14" rx="1.5" fill="none" stroke="#fff" stroke-width="1.6"/><path d="M1 2l9 7 9-7" fill="none" stroke="#fff" stroke-width="1.6"/></svg><span>info@fernwickfolks.com</span></div>
  </div>
  <div class="fcol" style="left:752px">
    <h4>Quick Links</h4>
    <ul><li>Home</li><li>About</li><li>Services</li><li>Contact Us</li><li>Client Portal</li></ul>
  </div>
  <div class="fcol" style="left:977px">
    <h4>Other Links</h4>
    <ul><li>FAQ</li><li>Blog</li><li>Free Quote</li><li>Privacy Policy</li><li>Terms of Service</li></ul>
  </div>
  <div class="abs" style="left:114px;top:384px;width:972px;height:1px;background:#3a3a3a"></div>
  <p class="abs" style="left:0;top:400px;width:1200px;text-align:center;font-size:12px;color:#ddd">Copyright © 2025 The Fernwick Folks. All rights reserved.</p>
</footer>

</body>
</html>
```